Thank You Card

I'm looking for a thank you card design using our logo and other graphics. We are an essential business and our employees (Electricians) have done an incredible job staying healthy and safe during the COVID-19 pandemic, I want to send each a thank you card.

```html
<!DOCTYPE html>
<html lang="en">
<head>
<meta charset="UTF-8">
<title>Thank You Card – Brightline Electric Co.</title>
<link rel="stylesheet" href="https://fonts.googleapis.com/css2?family=Arvo:wght@700&family=Montserrat:wght@400;600;800&display=swap">
<style>
  :root {
    --page-bg: #e9ecef;
    --card-light: #f4faff;
    --card-mid: #d6ecfa;
    --card-edge: #bfe0f6;
    --navy: #13248f;
    --ink: #1c1c24;
    --accent-red: #d8141d;
  }
  * { margin: 0; padding: 0; box-sizing: border-box; }
  html, body {
    width: 1200px;
    height: 1200px;
    overflow: hidden;
    background: var(--page-bg);
  }
  .canvas {
    width: 1200px;
    height: 1200px;
    display: flex;
    align-items: center;
    justify-content: center;
  }
  .thank-you-card {
    position: relative;
    width: 1000px;
    height: 572px;
    overflow: hidden;
    box-shadow: 0 10px 30px rgba(0, 0, 0, 0.18);
  }
  .card-backdrop {
    position: absolute;
    inset: 0;
    width: 100%;
    height: 100%;
  }
  .card-content {
    position: relative;
    height: 100%;
    display: flex;
    flex-direction: column;
    align-items: center;
    padding-top: 110px;
    text-align: center;
  }
  .brand-name {
    display: flex;
    align-items: center;
    gap: 12px;
    font-family: "Montserrat", sans-serif;
    font-weight: 800;
    font-size: 30px;
    letter-spacing: 0.5px;
    color: var(--accent-red);
    text-transform: uppercase;
  }
  .brand-dot {
    width: 18px;
    height: 18px;
    border-radius: 50%;
    background: var(--accent-red);
  }
  .headline {
    margin-top: 26px;
    font-family: "Arvo", serif;
    font-weight: 700;
    font-size: 118px;
    line-height: 1;
    color: var(--navy);
  }
  .message {
    margin-top: 26px;
    font-family: "Montserrat", sans-serif;
    font-weight: 400;
    font-size: 25px;
    line-height: 1.32;
    color: var(--ink);
    max-width: 640px;
  }
  .message .highlight {
    color: var(--accent-red);
    font-weight: 600;
  }
  .bottom-band {
    position: absolute;
    left: 0;
    right: 0;
    bottom: 0;
    height: 28px;
    background: var(--navy);
  }
</style>
</head>
<body>
  <main class="canvas">
    <article class="thank-you-card">
      <svg class="card-backdrop" viewBox="0 0 1000 572" preserveAspectRatio="none" role="img" aria-label="Soft light-blue background illustration of floating virus particles and bubbles">
        <defs>
          <radialGradient id="backdropGlow" cx="0.45" cy="0.3" r="0.8">
            <stop offset="0" stop-color="var(--card-light)"/>
            <stop offset="0.6" stop-color="var(--card-mid)"/>
            <stop offset="1" stop-color="var(--card-edge)"/>
          </radialGradient>
        </defs>
        <rect width="1000" height="572" fill="url(#backdropGlow)"/>
      </svg>

      <div class="card-content">
        <div class="brand-name">
          <span class="brand-dot"></span>
          <span>Brightline Electric Co.</span>
        </div>

        <h1 class="headline">Thank You</h1>

        <p class="message">
          We are an essential business and our employees (Electricians) have done an incredible job staying healthy and safe during the <span class="highlight">COVID-19</span> pandemic
        </p>
      </div>

      <div class="bottom-band"></div>
    </article>
  </main>
</body>
</html>
```